Looking for a creative label design for our retail coffee bags

We are a coffee manufacturer (coffee roaster) looking to re-brand our retail label for our coffee bags. Our main coffee blend that we sell is our Harborline Velvet Blend. You can use this name when creating the label. We are going for a look that represents our company as a coffee roaster. Please reference our website (www.brindlemugworks.com) and our Facebook page to learn more about our company and to give you more inspiration on creating this design.

Target Market(s)

Retail customers/grocery stores

Industry/Entity Type

Manufacturer

Requirements
Must have
• The size of the label has to be 3" width x 4" height

Logo must be Black
Nice to have
• We currently incorporate a color on our labels for each blend. For example, Harborline Velvet Blend (royal blue), Decaffeinated Blend (red), Breakfast Blend (green), Flavored coffees (gold).

Rustic/vintage style

```html
<!DOCTYPE html>
<html lang="en">
<head>
<meta charset="utf-8">
<title>Brindle Mugworks – Retail Coffee Labels</title>
<link rel="stylesheet" href="https://fonts.googleapis.com/css2?family=Lato:wght@400;700;900&display=swap">
<style>
  :root {
    --canvas: #ffffff;
    --frame: #b9b9bb;
    --pattern-light: #f4f4f4;
    --pattern-mid: #e2e2e2;
    --ink: #111111;
    --paper: #ffffff;
    --blend-red: #8e1b1f;
    --blend-gold: #c3932c;
    --blend-navy: #1f2453;
  }
  * { box-sizing: border-box; margin: 0; padding: 0; }
  html, body {
    width: 1200px;
    height: 1200px;
    overflow: hidden;
    background: var(--canvas);
    font-family: "Lato", Arial, sans-serif;
  }
  .label-row {
    position: absolute;
    left: 50px;
    top: 373px;
    display: flex;
    gap: 40px;
  }
  .label {
    position: relative;
    width: 340px;
    height: 453px;
    border: 4px solid var(--frame);
    background: var(--paper);
    display: flex;
    flex-direction: column;
  }
  .label__artwork {
    position: relative;
    height: 250px;
    background: radial-gradient(circle at 50% 40%, var(--pattern-light) 0%, var(--pattern-mid) 100%);
  }
  .brand-mark {
    position: absolute;
    left: 50%;
    top: 94px;
    width: 122px;
    height: 122px;
    transform: translate(-50%, -50%);
    border-radius: 50%;
    background: var(--paper);
    display: flex;
    align-items: center;
    justify-content: center;
  }
  .brand-mark__disc {
    width: 104px;
    height: 104px;
    border-radius: 50%;
    background: var(--ink);
    display: flex;
    align-items: center;
    justify-content: center;
    text-align: center;
  }
  .brand-mark__name {
    color: var(--paper);
    font-weight: 700;
    font-size: 14px;
    line-height: 1.1;
    letter-spacing: 1px;
    text-transform: uppercase;
  }
  .label__band {
    flex: 1;
    color: var(--paper);
    padding: 22px 26px 0 26px;
  }
  .label--red .label__band { background: var(--blend-red); }
  .label--gold .label__band { background: var(--blend-gold); }
  .label--navy .label__band { background: var(--blend-navy); }
  .blend-number {
    font-size: 17px;
    font-weight: 700;
    line-height: 1;
    padding-bottom: 7px;
    border-bottom: 1.5px solid var(--paper);
    width: 152px;
  }
  .blend-name {
    font-size: 22px;
    font-weight: 700;
    line-height: 1.05;
    text-transform: uppercase;
    padding: 8px 0 7px;
    border-bottom: 1.5px solid var(--paper);
    width: 196px;
  }
  .blend-notes {
    font-size: 7.2px;
    line-height: 1.35;
    width: 190px;
    margin-top: 9px;
  }
  .blend-weight {
    font-size: 12px;
    font-weight: 700;
    margin-top: 9px;
    padding-bottom: 7px;
    border-bottom: 1.5px solid var(--paper);
    width: 196px;
  }
</style>
</head>
<body>
  <main class="label-row">
    <article class="label label--red">
      <div class="label__artwork" role="img" aria-label="Hand-drawn coffee branch pattern with leaves and cherries in grey line work">
        <div class="brand-mark"><div class="brand-mark__disc"><span class="brand-mark__name">Brindle<br>Mugworks</span></div></div>
      </div>
      <section class="label__band">
        <p class="blend-number">01</p>
        <h2 class="blend-name">Harborline<br>Velvet Blend</h2>
        <p class="blend-notes">Lorem ipsum dolor sit amet, consectetuer adipiscing elit, sed diam nonummy nibh euismod tincidunt ut laoreet dolore magna aliquam erat volutpat. Ut wisi enim ad minim</p>
        <p class="blend-weight">16 oz</p>
      </section>
    </article>

    <article class="label label--gold">
      <div class="label__artwork" role="img" aria-label="Hand-drawn coffee branch pattern with leaves and cherries in grey line work">
        <div class="brand-mark"><div class="brand-mark__disc"><span class="brand-mark__name">Brindle<br>Mugworks</span></div></div>
      </div>
      <section class="label__band">
        <p class="blend-number">02</p>
        <h2 class="blend-name">Breakfast<br>Blend</h2>
        <p class="blend-notes">Lorem ipsum dolor sit amet, consectetuer adipiscing elit, sed diam nonummy nibh euismod tincidunt ut laoreet dolore magna aliquam erat volutpat. Ut wisi enim ad minim</p>
        <p class="blend-weight">16 oz</p>
      </section>
    </article>

    <article class="label label--navy">
      <div class="label__artwork" role="img" aria-label="Hand-drawn coffee branch pattern with leaves and cherries in grey line work">
        <div class="brand-mark"><div class="brand-mark__disc"><span class="brand-mark__name">Brindle<br>Mugworks</span></div></div>
      </div>
      <section class="label__band">
        <p class="blend-number">03</p>
        <h2 class="blend-name">House<br>Blend</h2>
        <p class="blend-notes">Lorem ipsum dolor sit amet, consectetuer adipiscing elit, sed diam nonummy nibh euismod tincidunt ut laoreet dolore magna aliquam erat volutpat. Ut wisi enim ad minim</p>
        <p class="blend-weight">16 oz</p>
      </section>
    </article>
  </main>
</body>
</html>
```